Corvett Tiling Solutions, QBCC 4870312, ABN 38204917586, Email corvetttiling@mailbox-demo.com,Mobile 04918365

Corvett Tiling Solutions, is the name of my wall and floor tiling company and the details above are needed on the business card. Im open to see what people come up with i really have no colour requirements or other design specs as long as its not too plain.

```html
<!DOCTYPE html>
<html lang="en">
<head>
<meta charset="utf-8">
<title>Corvett Tiling Solutions — Business Card</title>
<link rel="stylesheet" href="https://fonts.googleapis.com/css2?family=Lato:wght@400;700&display=swap">
<style>
  :root {
    --page-bg: #d9d4cc;
    --card-bg: #1d1d1e;
    --card-edge: #2a2a2b;
    --accent: #f5a623;
    --text-light: #ececec;
    --text-muted: #d6d6d6;
  }
  * { box-sizing: border-box; margin: 0; padding: 0; }
  html, body {
    width: 1200px;
    height: 1000px;
    overflow: hidden;
    background: var(--page-bg);
    font-family: "Lato", sans-serif;
  }
  .canvas {
    position: relative;
    width: 1200px;
    height: 1000px;
  }
  .card {
    position: absolute;
    left: 250px;
    width: 700px;
    height: 400px;
    border-radius: 22px;
    background: radial-gradient(ellipse at 40% 30%, var(--card-edge), var(--card-bg) 70%);
    box-shadow: 0 10px 28px rgba(0,0,0,0.28);
    color: var(--text-light);
  }
  .card--front { top: 60px; }
  .card--back { top: 540px; }

  .wordmark {
    display: flex;
    align-items: center;
    gap: 22px;
    color: var(--text-light);
    font-weight: 400;
  }
  .wordmark__square {
    width: 58px;
    height: 58px;
    background: var(--accent);
    flex: none;
  }
  .wordmark__name { display: flex; flex-direction: column; line-height: 1; }
  .wordmark__main { letter-spacing: 0.08em; }
  .wordmark__sub { letter-spacing: 0.09em; }

  .card--front .wordmark {
    position: absolute;
    left: 0; right: 0; top: 0; bottom: 0;
    justify-content: center;
  }
  .card--front .wordmark__main { font-size: 76px; }
  .card--front .wordmark__sub { font-size: 30px; margin-top: 10px; }

  .card--back .wordmark {
    position: absolute;
    left: 52px;
    top: 46px;
  }
  .card--back .wordmark__square { width: 46px; height: 46px; }
  .card--back .wordmark__main { font-size: 52px; }
  .card--back .wordmark__sub { font-size: 24px; margin-top: 6px; }

  .person {
    position: absolute;
    left: 56px;
    top: 170px;
  }
  .person__name {
    color: var(--accent);
    font-size: 28px;
    letter-spacing: 0.04em;
  }
  .person__role {
    font-size: 17px;
    letter-spacing: 0.08em;
    margin-top: 4px;
    color: var(--text-muted);
  }
  .contacts {
    position: absolute;
    left: 56px;
    top: 262px;
    list-style: none;
    font-size: 19px;
    line-height: 1.32;
    letter-spacing: 0.04em;
    color: var(--text-light);
  }
  .contacts__label {
    color: var(--accent);
    font-weight: 700;
  }
</style>
</head>
<body>
  <main class="canvas">
    <section class="card card--front" aria-label="Card front">
      <div class="wordmark">
        <span class="wordmark__square"></span>
        <span class="wordmark__name">
          <span class="wordmark__main">CORVETT</span>
          <span class="wordmark__sub">TILING SOLUTIONS</span>
        </span>
      </div>
    </section>

    <section class="card card--back" aria-label="Card back">
      <div class="wordmark">
        <span class="wordmark__square"></span>
        <span class="wordmark__name">
          <span class="wordmark__main">CORVETT</span>
          <span class="wordmark__sub">TILING SOLUTIONS</span>
        </span>
      </div>
      <div class="person">
        <p class="person__name">YOUR NAME</p>
        <p class="person__role">Director</p>
      </div>
      <ul class="contacts">
        <li><span class="contacts__label">M:</span> 04918365</li>
        <li><span class="contacts__label">E:</span> corvetttiling@mailbox-demo.com</li>
        <li><span class="contacts__label">QBCC</span> 4870312</li>
        <li><span class="contacts__label">ABN</span> 38204917586</li>
      </ul>
    </section>
  </main>
</body>
</html>
```